Music Festival Business Cards

The Lanternmoor Festival
Produced by Bramblewick Sound Group LLC
New music festival in Arkansas.

Target Market(s)

18-35 year olds

Industry/Entity Type

Festival

Contact Information for Business Card

We are a 5-partner team producing a music festival in Arkansas. We need slick business cards, and I want them to be square.

Requirements
Must have
• I NEED THESE TO BE IN SQUARE SIZE - 2x2 or 2.5x2.5... please not regular size.
• I need www.thelanternmoor.live as the link to website.

```html
<!DOCTYPE html>
<html lang="en">
<head>
<meta charset="utf-8">
<title>The Lanternmoor Festival – Square Business Cards</title>
<link rel="stylesheet" href="https://fonts.googleapis.com/css2?family=Tinos:wght@400;700&display=swap">
<style>
  :root {
    --backdrop: #3b3431;
    --card: #141414;
    --card-edge: #0c0c0c;
    --gloss: #3c3c3c;
    --ink-light: #c9c9c9;
    --accent: #1fa3a6;
    --accent-ink: #0e1414;
  }
  * { box-sizing: border-box; margin: 0; padding: 0; }
  html, body {
    width: 1200px;
    height: 810px;
    overflow: hidden;
    background: var(--backdrop);
    font-family: "Tinos", "Times New Roman", serif;
  }
  .sheet {
    width: 1200px;
    height: 810px;
    display: flex;
    align-items: center;
    justify-content: center;
    gap: 40px;
  }
  .card {
    width: 460px;
    height: 460px;
    background: var(--card);
    border: 1px solid var(--card-edge);
    position: relative;
  }
  /* Front */
  .card--front {
    display: flex;
    align-items: center;
    justify-content: center;
  }
  .front-wordmark {
    font-size: 38px;
    font-weight: 700;
    letter-spacing: 3px;
    color: var(--gloss);
    text-transform: uppercase;
  }
  /* Back */
  .card--back { padding: 70px 0 0 84px; }
  .back-wordmark {
    position: absolute;
    top: 78px;
    right: 60px;
    display: flex;
    align-items: center;
    gap: 10px;
    font-size: 22px;
    color: var(--accent);
  }
  .back-wordmark .mark-square {
    width: 14px;
    height: 14px;
    background: var(--accent);
  }
  .person {
    margin-top: 110px;
  }
  .person-name {
    font-size: 30px;
    color: var(--ink-light);
    line-height: 1;
  }
  .person-role {
    font-size: 18px;
    color: var(--accent);
    margin-top: 4px;
  }
  .contact-list {
    list-style: none;
    margin-top: 22px;
  }
  .contact-item {
    display: flex;
    align-items: center;
    gap: 12px;
    font-size: 20px;
    color: var(--ink-light);
    margin-bottom: 10px;
  }
  .contact-icon {
    width: 15px;
    height: 15px;
    flex: none;
  }
</style>
</head>
<body>
<main class="sheet">
  <section class="card card--front" aria-label="Card front">
    <span class="front-wordmark">The Lanternmoor</span>
  </section>

  <section class="card card--back" aria-label="Card back">
    <div class="back-wordmark"><span class="mark-square"></span><span>The Lanternmoor</span></div>

    <div class="person">
      <p class="person-name">Rowan Ellery</p>
      <p class="person-role">Service Manager</p>
    </div>

    <ul class="contact-list">
      <li class="contact-item">
        <svg class="contact-icon" viewBox="0 0 16 16" aria-hidden="true">
          <rect width="16" height="16" fill="var(--accent)"/>
          <rect x="3" y="5" width="10" height="7" fill="none" stroke="var(--accent-ink)" stroke-width="1.3"/>
          <path d="M3 5 L8 9 L13 5" fill="none" stroke="var(--accent-ink)" stroke-width="1.3"/>
        </svg>
        <span>info@thelanternmoor.live</span>
      </li>
      <li class="contact-item">
        <svg class="contact-icon" viewBox="0 0 16 16" aria-hidden="true">
          <rect width="16" height="16" fill="var(--accent)"/>
          <circle cx="8" cy="8" r="4.5" fill="none" stroke="var(--accent-ink)" stroke-width="1.3"/>
          <path d="M3.5 8 H12.5 M8 3.5 C5.5 6 5.5 10 8 12.5 M8 3.5 C10.5 6 10.5 10 8 12.5" fill="none" stroke="var(--accent-ink)" stroke-width="1"/>
        </svg>
        <span>www.thelanternmoor.live</span>
      </li>
      <li class="contact-item">
        <svg class="contact-icon" viewBox="0 0 16 16" aria-hidden="true">
          <rect width="16" height="16" fill="var(--accent)"/>
          <path d="M5 3.5 L7 3.5 L7.5 6 L6.3 7 C7 8.6 7.6 9.2 9 9.8 L10 8.6 L12.5 9.1 L12.5 11 C12.5 12 11.5 12.5 10.5 12.3 C7 11.5 4.5 9 3.8 5.5 C3.6 4.5 4 3.5 5 3.5 Z" fill="var(--accent-ink)"/>
        </svg>
        <span>501-555-0142</span>
      </li>
      <li class="contact-item">
        <svg class="contact-icon" viewBox="0 0 16 16" aria-hidden="true">
          <rect width="16" height="16" fill="var(--accent)"/>
          <rect x="4" y="6.5" width="8" height="5" fill="none" stroke="var(--accent-ink)" stroke-width="1.3"/>
          <rect x="5.5" y="3.5" width="5" height="3" fill="var(--accent-ink)"/>
        </svg>
        <span>501-555-0187</span>
      </li>
    </ul>
  </section>
</main>
</body>
</html>
```